Lawn mowing business card design

We need a business card design for our lawn mowing and gardening business which is located in the Northern Beaches of Sydney. Our business name is Copperleaf Yards and our logo is predominantly green and yellow in color. Please see our website at www.copperleafyards.com.au for design ideas. The business targets young professionals and older clientele. As such the font should be easy to read, but I also want the business card to be colorful and stand out.

Target Market(s)

young professionals

Industry/Entity Type

Lawn Care

Contact Information for Business Card

Copperleaf Yards, Martin Kealey, 0478650912, www.copperleafyards.com.au, email: copperleafyards@mailbox-example.com

Font styles to use
Serif

Colors
9bcb3b
fbed22

Requirements
Must have
• Must include the details listed above. Must include the attached logo.
Nice to have
• Logo attached with two copies. The logo without any writing is high quality, please feel free to be creative with the text stating our business name "Copperleaf Yards" using this file.

```html
<!DOCTYPE html>
<html lang="en">
<head>
<meta charset="utf-8">
<title>Copperleaf Yards – Business Card</title>
<link rel="stylesheet" href="https://fonts.googleapis.com/css2?family=Alfa+Slab+One&display=swap">
<style>
  :root {
    --page-bg: #e6e7e9;
    --card-white: #ffffff;
    --brand-yellow: #fbed22;
    --brand-green: #9bcb3b;
    --green-light: #b3e04a;
    --grass-deep: #3f9a2a;
    --grass-mid: #6cc23a;
    --ground-band: #62b56c;
    --logo-green: #2f8a3a;
    --ink: #111111;
    --text-white: #ffffff;
    --shadow: rgba(0, 0, 0, 0.18);
  }
  * { box-sizing: border-box; margin: 0; padding: 0; }
  html, body {
    width: 1200px;
    height: 800px;
    overflow: hidden;
    background: var(--page-bg);
    font-family: "Alfa Slab One", Georgia, serif;
  }
  .canvas {
    position: relative;
    width: 1200px;
    height: 800px;
    display: flex;
    align-items: center;
    justify-content: center;
    gap: 40px;
  }
  .card {
    position: relative;
    width: 540px;
    height: 310px;
    background: var(--card-white);
    overflow: hidden;
    box-shadow: 0 10px 28px var(--shadow);
  }

  /* Brand name block (stands in for the mark) */
  .brand {
    position: absolute;
    display: flex;
    align-items: center;
    gap: 10px;
    color: var(--logo-green);
    font-size: 22px;
    white-space: nowrap;
  }
  .brand-dot {
    width: 22px;
    height: 22px;
    border-radius: 50%;
    background: var(--brand-yellow);
    flex: none;
  }

  /* Front card */
  .card--front .brand {
    left: 50%;
    top: 92px;
    transform: translateX(-50%);
    font-size: 26px;
  }
  .grass-art {
    position: absolute;
    left: 0;
    right: 0;
    top: 140px;
    height: 132px;
    background: linear-gradient(to bottom,
      rgba(108, 194, 58, 0) 0%,
      var(--grass-mid) 45%,
      var(--grass-deep) 100%);
  }
  .ground-band {
    position: absolute;
    left: 0;
    right: 0;
    bottom: 0;
    height: 38px;
    background: var(--ground-band);
  }

  /* Back card */
  .back-shapes {
    position: absolute;
    inset: 0;
  }
  .card--back .brand {
    left: 145px;
    top: 48px;
  }
  .title {
    position: absolute;
    left: 95px;
    top: 168px;
    font-size: 30px;
    color: var(--ink);
    letter-spacing: 0.5px;
    transform: rotate(-8.4deg);
    transform-origin: left center;
    white-space: nowrap;
  }
  .contact-list {
    position: absolute;
    left: 215px;
    top: 222px;
    list-style: none;
    transform: rotate(-8.4deg);
    transform-origin: left top;
  }
  .contact-item {
    display: flex;
    align-items: center;
    gap: 6px;
    color: var(--text-white);
    font-size: 12.5px;
    line-height: 20px;
    white-space: nowrap;
  }
  .contact-icon {
    width: 16px;
    height: 16px;
    flex: none;
  }
</style>
</head>
<body>
<main class="canvas">

  <section class="card card--front" aria-label="Business card front">
    <div class="grass-art" role="img" aria-label="Illustration of tall green grass blades across the card"></div>
    <div class="ground-band"></div>
    <div class="brand"><span class="brand-dot"></span>Copperleaf Yards</div>
  </section>

  <section class="card card--back" aria-label="Business card back">
    <svg class="back-shapes" viewBox="0 0 540 310" preserveAspectRatio="none" aria-hidden="true">
      <defs>
        <linearGradient id="greenFill" x1="0" y1="0" x2="1" y2="1">
          <stop offset="0" stop-color="var(--brand-green)"/>
          <stop offset="1" stop-color="var(--green-light)"/>
        </linearGradient>
      </defs>
      <polygon points="0,188 540,108 540,158 0,248" fill="var(--brand-yellow)"/>
      <polygon points="0,248 540,158 540,310 0,310" fill="url(#greenFill)"/>
    </svg>

    <div class="brand"><span class="brand-dot"></span>Copperleaf Yards</div>

    <h1 class="title">COPPERLEAF YARDS</h1>

    <ul class="contact-list">
      <li class="contact-item">
        <svg class="contact-icon" viewBox="0 0 16 16" aria-hidden="true">
          <circle cx="8" cy="8" r="7.5" fill="var(--brand-yellow)"/>
          <path d="M5 4.5l1.6-.4 1 2-1 .8a5 5 0 0 0 2.5 2.5l.8-1 2 1-.4 1.6c-3.5.3-6.8-3-6.5-6.5z" fill="var(--text-white)"/>
        </svg>
        047-865-0912
      </li>
      <li class="contact-item">
        <svg class="contact-icon" viewBox="0 0 16 16" aria-hidden="true">
          <circle cx="8" cy="8" r="7.5" fill="var(--brand-yellow)"/>
          <rect x="4" y="5.2" width="8" height="5.6" fill="var(--text-white)"/>
          <path d="M4 5.2l4 3 4-3" fill="none" stroke="var(--brand-yellow)" stroke-width="0.9"/>
        </svg>
        copperleafyards@mailbox-example.com
      </li>
      <li class="contact-item">
        <svg class="contact-icon" viewBox="0 0 16 16" aria-hidden="true">
          <circle cx="8" cy="8" r="7.5" fill="var(--brand-yellow)"/>
          <circle cx="8" cy="8" r="4" fill="none" stroke="var(--text-white)" stroke-width="1"/>
          <ellipse cx="8" cy="8" rx="1.7" ry="4" fill="none" stroke="var(--text-white)" stroke-width="0.9"/>
          <line x1="4" y1="8" x2="12" y2="8" stroke="var(--text-white)" stroke-width="0.9"/>
        </svg>
        www.copperleafyards.com.au
      </li>
    </ul>
  </section>

</main>
</body>
</html>
```